Front cover for our tenth anniversary show programme

To create an eye catching tenth anniversary front cover for our programme

Moonbrook presents DANCE! 2015

date of the show Sunday 3rd May 2015

Venue The Harrowgate Stagehouse

please see the updated brief!

Reason: there hasn't been anything that is quite right

```html
<!DOCTYPE html>
<html lang="en">
<head>
<meta charset="utf-8">
<title>Moonbrook presents DANCE! 2015 – Programme Cover</title>
<link rel="stylesheet" href="https://fonts.googleapis.com/css2?family=Raleway:wght@200;300;700;800&display=swap">
<style>
  :root {
    --page-bg: #eeeeee;
    --plum-deep: #3e0420;
    --plum-mid: #6e0a3c;
    --magenta: #93134f;
    --title-pink: #f3a9c9;
    --accent-pink: #ff4fa3;
    --white: #ffffff;
    --skin-light: #f2d9cc;
    --skin-mid: #e5c0ae;
    --ribbon: #e889b4;
    --satin: #efdcc4;
    --stage-red: #8c1f1a;
    --stage-amber: #c0582c;
  }
  * { box-sizing: border-box; margin: 0; padding: 0; }
  html, body {
    width: 1200px;
    height: 1200px;
    overflow: hidden;
    background: var(--page-bg);
  }
  .canvas {
    position: relative;
    width: 1200px;
    height: 1200px;
  }
  .programme-cover {
    position: absolute;
    left: 210px;
    top: 50px;
    width: 780px;
    height: 1100px;
    overflow: hidden;
    background:
      radial-gradient(ellipse 75% 60% at 55% 62%, var(--magenta) 0%, var(--plum-mid) 55%, var(--plum-deep) 100%);
    font-family: "Raleway", "Helvetica Neue", Arial, sans-serif;
    color: var(--white);
  }
  .hero-photo {
    position: absolute;
    left: 0;
    top: 0;
    width: 370px;
    height: 1060px;
    background:
      linear-gradient(180deg, rgba(242,217,204,0.0) 0%, rgba(242,217,204,0.9) 8%, var(--skin-mid) 30%, var(--ribbon) 48%, var(--satin) 62%, var(--satin) 88%, rgba(239,220,196,0) 100%);
    -webkit-mask-image: linear-gradient(90deg, #000 0%, #000 70%, transparent 100%);
            mask-image: linear-gradient(90deg, #000 0%, #000 70%, transparent 100%);
  }
  .anniversary-mark {
    position: absolute;
    left: 420px;
    top: 60px;
    width: 300px;
    text-align: center;
  }
  .brand-name {
    display: inline-flex;
    align-items: center;
    gap: 14px;
    font-weight: 700;
    font-size: 56px;
    letter-spacing: 0.5px;
    color: var(--white);
  }
  .brand-dot {
    width: 22px;
    height: 22px;
    border-radius: 50%;
    background: var(--accent-pink);
  }
  .anniversary-line {
    margin-top: 6px;
    font-weight: 700;
    font-size: 22px;
    color: var(--white);
    line-height: 1.05;
  }
  .anniversary-years {
    display: block;
    font-weight: 800;
    font-size: 40px;
    color: var(--accent-pink);
    letter-spacing: -0.5px;
  }
  .show-title {
    position: absolute;
    left: 395px;
    top: 375px;
    width: 360px;
    text-align: right;
    font-weight: 200;
    color: var(--title-pink);
    line-height: 1.0;
  }
  .show-title .line { display: block; }
  .show-title .line-brand { font-size: 68px; }
  .show-title .line-presents { font-size: 50px; }
  .show-title .line-dance { font-size: 72px; }
  .show-title .line-year { font-size: 72px; }
  .performance-strip {
    position: absolute;
    left: 400px;
    top: 735px;
    width: 345px;
    height: 118px;
    border: 2px solid rgba(255,255,255,0.55);
    background:
      linear-gradient(90deg, var(--stage-red) 0%, var(--stage-amber) 30%, #2a0d12 48%, #d9c7d2 62%, #5b2740 80%, #c8b3c4 100%);
  }
  .show-details {
    position: absolute;
    left: 400px;
    top: 955px;
    width: 360px;
    font-weight: 700;
    font-size: 29px;
    line-height: 1.35;
    color: var(--white);
  }
</style>
</head>
<body>
  <div class="canvas">
    <section class="programme-cover">
      <div class="hero-photo" role="img" aria-label="Photograph of a dancer's hands tying pink satin ribbons around a pointe shoe, foot en pointe"></div>

      <div class="anniversary-mark">
        <div class="brand-name"><span class="brand-dot"></span>Moonbrook</div>
        <div class="anniversary-line">Celebrating <span class="anniversary-years">Ten Years</span></div>
      </div>

      <h1 class="show-title">
        <span class="line line-brand">Moonbrook</span>
        <span class="line line-presents">presents</span>
        <span class="line line-dance">DANCE!</span>
        <span class="line line-year">2015</span>
      </h1>

      <div class="performance-strip" role="img" aria-label="Strip of stage photographs showing dancers performing in costume under coloured lights"></div>

      <p class="show-details">
        Sunday 3rd May 2015<br>
        The Harrowgate Stagehouse
      </p>
    </section>
  </div>
</body>
</html>
```